Job advert for Forged Here Collective

I would like a poster graphic that I can promote on social media to advertise a job vacancy we will be promoting our upcoming jobs, here is the text...

WE ARE ON THE…

LOOKOUT
(maybe insert graphic or icon that fits with the message here)

For A

OPERATIONS AND HR MANAGER

MEMBERSHIP ADVISOR (EAST MIDLANDS)

SOCIAL MEDIA CONTENT CREATOR

THE UK’s FASTEST GROWING NETWORK FOR MANUFACTURERS

OFFICES IN BIRMINGHAM AND LEEDS - WE ARE AN INCLUSIVE EMPLOYER (use the equality logo provided here)

Target Market(s)

people looking to find a new job

Industry/Entity Type

Manufacture

Font styles to use
Sans Serif

Colors
f04a50
f68e4e
e667a6

Requirements
Must have
• Clear simple and contemporary style
Nice to have
• a nice graphic or icon to convey the text message
Should not have
• use of dark depressing colours

```html
<!DOCTYPE html>
<html lang="en">
<head>
<meta charset="utf-8">
<title>Forged Here Collective – We Are On The Lookout</title>
<link href="https://fonts.googleapis.com/css2?family=Cabin:wght@400;500;600;700&display=swap" rel="stylesheet">
<style>
  :root {
    --paper: #ffffff;
    --ink-grey: #7a7a7a;
    --ink-soft: #8c8c8c;
    --rule: #c9c9c9;
    --brand-green: #a6cc35;
    --warm-red: #c9292e;
    --warm-coral: #f04a50;
    --warm-orange: #f68e4e;
    --deep-red: #7d1d22;
  }
  * { margin: 0; padding: 0; box-sizing: border-box; }
  html, body { width: 900px; height: 1200px; overflow: hidden; background: var(--paper); }
  .poster {
    position: relative;
    width: 900px;
    height: 1200px;
    background: var(--paper);
    font-family: "Cabin", sans-serif;
    color: var(--ink-grey);
    overflow: hidden;
  }
  .brand {
    position: absolute;
    left: 101px;
    top: 96px;
    display: flex;
    align-items: center;
    gap: 14px;
  }
  .brand-dot {
    width: 88px;
    height: 88px;
    border-radius: 50%;
    background: var(--brand-green);
  }
  .brand-name {
    font-size: 28px;
    font-weight: 500;
    line-height: 1.05;
    color: var(--brand-green);
    text-transform: uppercase;
    letter-spacing: 0.5px;
  }
  .headline {
    position: absolute;
    left: 200px;
    top: 214px;
    text-transform: uppercase;
  }
  .headline-lead {
    display: block;
    font-size: 66px;
    font-weight: 400;
    color: var(--ink-soft);
    line-height: 1;
    letter-spacing: 0.5px;
  }
  .headline-key {
    display: block;
    font-size: 64px;
    font-weight: 700;
    color: var(--ink-grey);
    line-height: 1;
    margin-top: 8px;
    letter-spacing: 0.5px;
  }
  .lookout-disc {
    position: absolute;
    left: 398px;
    top: 307px;
    width: 436px;
    height: 436px;
    border-radius: 50%;
    background: var(--brand-green);
  }
  .roles {
    position: absolute;
    left: 203px;
    top: 733px;
    width: 635px;
    list-style: none;
    font-size: 17px;
    color: var(--ink-grey);
    text-transform: uppercase;
  }
  .roles li {
    height: 40px;
    line-height: 36px;
    border-bottom: 1px solid var(--rule);
    white-space: nowrap;
  }
  .roles li.intro { text-transform: none; height: 36px; line-height: 30px; }
  .roles li:last-child { border-bottom: none; }
  .roles strong { font-weight: 700; color: #666; }
  .warm-wave {
    position: absolute;
    left: 0;
    top: 0;
    width: 900px;
    height: 1200px;
  }
  .inclusion-badge {
    position: absolute;
    left: 205px;
    top: 997px;
    width: 80px;
    height: 80px;
    border-radius: 50%;
    background: radial-gradient(circle at 40% 40%, var(--warm-orange), var(--warm-coral) 60%, var(--warm-red));
  }
  .badge-divider {
    position: absolute;
    left: 458px;
    top: 935px;
    width: 1px;
    height: 140px;
    background: var(--rule);
  }
</style>
</head>
<body>
<main class="poster">
  <svg class="warm-wave" viewBox="0 0 900 1200" aria-hidden="true">
    <defs>
      <linearGradient id="warmFill" x1="0" y1="0" x2="1" y2="1">
        <stop offset="0" stop-color="#e85a2c"/>
        <stop offset="0.35" stop-color="#d2362c"/>
        <stop offset="1" stop-color="#c2262f"/>
      </linearGradient>
    </defs>
    <rect x="30" y="839" width="841" height="334" fill="url(#warmFill)"/>
    <path d="M260 900 C 290 1040 360 1120 470 1173 L 400 1173 C 320 1110 275 1010 260 900 Z" fill="var(--deep-red)" opacity="0.55"/>
    <path d="M30 839 C 70 1080 300 1172 470 1168 C 680 1162 835 1060 871 919 L 871 820 L 30 820 Z" fill="var(--paper)"/>
    <path d="M871 919 C 860 960 845 990 830 1010 L 871 1000 Z" fill="var(--warm-orange)" opacity="0.6"/>
  </svg>

  <header class="brand">
    <span class="brand-dot"></span>
    <span class="brand-name">Forged Here<br>Collective</span>
  </header>

  <h1 class="headline">
    <span class="headline-lead">We are on the…</span>
    <span class="headline-key">Lookout</span>
  </h1>

  <div class="lookout-disc"></div>

  <ul class="roles">
    <li class="intro">For A</li>
    <li><strong>Operations</strong> and <strong>HR Manager</strong></li>
    <li><strong>Membership Advisor</strong> (East Midlands)</li>
    <li><strong>Social Media Content Creator</strong></li>
    <li>The UK’s fastest growing network for manufacturers</li>
    <li>Offices in Birmingham and Leeds - we are an inclusive employer</li>
  </ul>

  <div class="inclusion-badge" role="img" aria-label="Inclusive employer badge"></div>
  <div class="badge-divider"></div>
</main>
</body>
</html>
```